New Business Card Design Project

Easy part first... I want the backside to be simple... jet black background with our logo in jet black/white/color. Feel free to play with tagline ideas under the logo if you want, I'm still toying around with it myself.

The front side... I need the logo on it, my photo headshot, and the following information:

Ray T. Calloway
Top Producer
555-201-4837
calloway.ray.t@fernmail.example
www.listnorthernnests.example
www.getnorthernnests.example

I'm looking for creativity with font, simple, but elegant, pairs well with the logo, good visibility of my photo, black background on the front as well, clearly see and identify information.
Updates

I would like the websites to have capitalization on the first letter of each word - www.ListNorthernNests.example and www.GetNorthernNests.example Also, I would like each of the capital letters to be slightly larger than the other font

Target Market(s)

We help people buy and sell homes from $50,000 to over a $1million.

Industry/Entity Type

Business

Requirements
Must have
• Must have information from above.
Nice to have
• Introducing a new color to be sharp against the black- possibly in the silver/nickel/platinum metallics? Feel free to crop the headshot down some if needed.
Should not have
• NO CHEESY GRAPHICS

```html
<!DOCTYPE html>
<html lang="en">
<head>
<meta charset="utf-8">
<title>Northern Nest Realty – Business Card</title>
<link rel="stylesheet" href="https://fonts.googleapis.com/css2?family=Cinzel:wght@600&family=Open+Sans:wght@400&display=swap">
<style>
  :root {
    --page: #e4e1dc;
    --card: #050505;
    --ink: #ffffff;
    --accent: #b8a46a;
    --photo-dark: #2e241d;
    --photo-light: #6b5a4c;
  }
  html, body {
    margin: 0;
    width: 1200px;
    height: 1000px;
    overflow: hidden;
    background: var(--page);
  }
  .card {
    position: absolute;
    left: 194px;
    width: 812px;
    height: 464px;
    background: var(--card);
    color: var(--ink);
    box-shadow: 0 6px 18px rgba(0,0,0,.25);
    overflow: hidden;
  }
  .card--back { top: 24px; }
  .card--front { top: 512px; }

  .brand {
    position: absolute;
    display: flex;
    align-items: center;
    gap: 12px;
    font-family: "Cinzel", serif;
    font-weight: 600;
    color: var(--ink);
    white-space: nowrap;
  }
  .brand__mark {
    width: 14px;
    height: 14px;
    background: var(--accent);
  }
  .card--back .brand {
    left: 50%;
    top: 50%;
    transform: translate(-50%, -50%);
    font-size: 44px;
    letter-spacing: 1px;
  }
  .card--back .brand__mark { width: 22px; height: 22px; }
  .card--front .brand {
    left: 602px;
    top: 120px;
    transform: translateX(-50%);
    font-size: 25px;
  }

  .headshot {
    position: absolute;
    left: 100px;
    top: 50px;
    width: 206px;
    height: 232px;
    background: radial-gradient(circle at 40% 35%, var(--photo-light), var(--photo-dark));
  }
  .agent {
    position: absolute;
    left: 86px;
    top: 292px;
    font-family: "Open Sans", sans-serif;
  }
  .agent__name {
    margin: 0;
    font-size: 30px;
    font-weight: 400;
    letter-spacing: 1px;
    line-height: 1.2;
  }
  .agent__title {
    margin: 2px 0 0 -8px;
    font-size: 19px;
    letter-spacing: 2px;
  }
  .divider {
    position: absolute;
    left: 380px;
    top: 66px;
    width: 2px;
    height: 330px;
    background: var(--ink);
  }
  .contact {
    position: absolute;
    left: 428px;
    top: 238px;
    margin: 0;
    padding: 0;
    list-style: none;
    font-family: "Open Sans", sans-serif;
    font-size: 20px;
    letter-spacing: .2px;
  }
  .contact li {
    display: flex;
    align-items: center;
    gap: 10px;
    height: 36px;
    white-space: nowrap;
  }
  .contact .cap {
    font-size: 1.15em;
    line-height: 1;
  }
  .contact svg {
    width: 20px;
    height: 20px;
    flex: none;
    fill: none;
    stroke: var(--ink);
    stroke-width: 1.6;
  }
</style>
</head>
<body>

<section class="card card--back" aria-label="Card back">
  <div class="brand"><span class="brand__mark"></span>Northern Nest Realty</div>
</section>

<section class="card card--front" aria-label="Card front">
  <div class="headshot" role="img" aria-label="Agent headshot photograph"></div>
  <div class="agent">
    <h1 class="agent__name">Ray T. Calloway</h1>
    <p class="agent__title">Top Producer</p>
  </div>

  <div class="divider"></div>

  <div class="brand"><span class="brand__mark"></span>Northern Nest Realty</div>

  <ul class="contact">
    <li>
      <svg viewBox="0 0 20 20"><path d="M5 2 L8 2 L9 6 L7 8 Q9 12 12 13 L14 11 L18 12 L18 15 Q17 18 14 18 Q4 16 2 6 Q2 3 5 2 Z"/></svg>
      <span>555-201-4837</span>
    </li>
    <li>
      <svg viewBox="0 0 20 20"><rect x="2" y="4" width="16" height="12"/><path d="M2 4 L10 11 L18 4"/></svg>
      <span>calloway.ray.t@fernmail.example</span>
    </li>
    <li>
      <svg viewBox="0 0 20 20"><circle cx="10" cy="10" r="8"/><ellipse cx="10" cy="10" rx="3.5" ry="8"/><path d="M2 10 H18 M3.5 6 H16.5 M3.5 14 H16.5"/></svg>
      <span>www.<span class="cap">L</span>ist<span class="cap">N</span>orthern<span class="cap">N</span>ests.example</span>
    </li>
    <li>
      <svg viewBox="0 0 20 20"><circle cx="10" cy="10" r="8"/><ellipse cx="10" cy="10" rx="3.5" ry="8"/><path d="M2 10 H18 M3.5 6 H16.5 M3.5 14 H16.5"/></svg>
      <span>www.<span class="cap">G</span>et<span class="cap">N</span>orthern<span class="cap">N</span>ests.example</span>
    </li>
  </ul>
</section>

</body>
</html>
```